Psychiatrist/ Psychotherapist needs a letterhead design

I am a Psychiatrist working in private practice. I work as a psychotherapist and treat patients with depression, anxiety, post traumatic stress and relationship problems. I need a letterhead which is elegant and professional. I would like to see designs using colours such as blues and greys.
I would like the information on the letterhead split between the top and bottom of the page to give it a look of balance.
I want it to look elegant, feminine and upmarket. I don't want it to look too corporate but to show some flair and to be a bit artistic.

Other doctors, specialists and agencies who have referred patients to me.

Work

Script

Requirements
Must have
• My name and my profession psychiatrist need to be highlighted and prominent. It needs to be professional looking and elegant without being old fashioned or too conservative.
Nice to have
• Balance between the top and bottom of the page.
Should not have
• I don't want fonts which are old and too traditional.

```html
<!DOCTYPE html>
<html lang="en">
<head>
<meta charset="utf-8">
<title>Letterhead – Dr Helena Marlowe K., Psychiatrist</title>
<link rel="stylesheet" href="https://fonts.googleapis.com/css2?family=Montserrat:wght@300;400;600&display=swap">
<style>
  :root {
    --backdrop: #e9e9e9;
    --paper: #ffffff;
    --brand-blue: #1f74b8;
    --accent-grey: #9b9b9b;
    --text-grey: #7a7a7a;
  }
  * { box-sizing: border-box; margin: 0; padding: 0; }
  html, body {
    width: 1200px;
    height: 936px;
    overflow: hidden;
    background: var(--backdrop);
    font-family: "Montserrat", Arial, sans-serif;
  }
  .letterhead {
    position: absolute;
    left: 300px;
    top: 44px;
    width: 600px;
    height: 848px;
    background: var(--paper);
    box-shadow: 0 2px 10px rgba(0,0,0,0.08);
  }
  .identity {
    position: absolute;
    top: 58px;
    right: 48px;
    text-align: right;
  }
  .identity__name {
    font-weight: 600;
    font-size: 19px;
    letter-spacing: -0.2px;
    color: var(--brand-blue);
    text-transform: uppercase;
  }
  .identity__profession {
    margin-top: 3px;
    font-weight: 400;
    font-size: 10px;
    letter-spacing: 0.6px;
    color: var(--text-grey);
    text-transform: uppercase;
  }
  .contact {
    position: absolute;
    top: 78px;
    left: 44px;
    list-style: none;
    font-weight: 300;
    font-size: 8.5px;
    line-height: 13px;
    color: var(--text-grey);
  }
  .contact__item {
    display: flex;
    align-items: center;
    gap: 5px;
  }
  .contact__icon {
    width: 9px;
    height: 9px;
    flex: none;
  }
  .contact__item--address { margin-top: 4px; padding-left: 14px; }
  .footer-band {
    position: absolute;
    left: 0;
    right: 0;
    bottom: 0;
    height: 9px;
  }
  .footer-band__grey {
    position: absolute;
    left: 0; top: 0; bottom: 0;
    width: 45%;
    background: var(--accent-grey);
  }
  .footer-band__blue {
    position: absolute;
    right: 0; top: 0; bottom: 0;
    width: 54%;
    background: var(--brand-blue);
  }
</style>
</head>
<body>
  <main class="letterhead">
    <header class="identity">
      <h1 class="identity__name">Dr Helena Marlowe K.</h1>
      <p class="identity__profession">Psychiatrist</p>
    </header>

    <ul class="contact">
      <li class="contact__item">
        <svg class="contact__icon" viewBox="0 0 10 10"><circle cx="5" cy="5" r="4.5" fill="var(--brand-blue)"/><path d="M3.3 2.8c.3-.2.6-.1.7.2l.4.8c.1.2 0 .4-.2.5l-.3.2c.3.7.8 1.2 1.5 1.5l.2-.3c.1-.2.3-.3.5-.2l.8.4c.3.1.4.4.2.7l-.3.4c-.2.2-.5.3-.8.2C4.6 6.8 3.2 5.4 2.8 3.9c-.1-.3 0-.6.2-.8z" fill="#fff"/></svg>
        (08) 8412 5730
      </li>
      <li class="contact__item">
        <svg class="contact__icon" viewBox="0 0 10 10"><circle cx="5" cy="5" r="4.5" fill="var(--brand-blue)"/><rect x="3" y="2.6" width="4" height="2" fill="#fff"/><rect x="2.5" y="4.6" width="5" height="2.8" rx="0.4" fill="#fff"/></svg>
        (08) 8412 5731
      </li>
      <li class="contact__item">
        <svg class="contact__icon" viewBox="0 0 10 10"><circle cx="5" cy="5" r="4.5" fill="var(--brand-blue)"/><rect x="3.6" y="2.2" width="2.8" height="5.6" rx="0.5" fill="#fff"/></svg>
        0418662907
      </li>
      <li class="contact__item">
        <svg class="contact__icon" viewBox="0 0 10 10"><circle cx="5" cy="5" r="4.5" fill="var(--brand-blue)"/><rect x="2.6" y="3.2" width="4.8" height="3.6" fill="#fff"/><path d="M2.6 3.2L5 5.2l2.4-2" fill="none" stroke="var(--brand-blue)" stroke-width="0.6"/></svg>
        hmarlowe@rivermail.net.au
      </li>
      <li class="contact__item contact__item--address">14 Linden Avenue, Norwood, SA 5067</li>
    </ul>

    <div class="footer-band" aria-hidden="true">
      <span class="footer-band__grey"></span>
      <span class="footer-band__blue"></span>
    </div>
  </main>
</body>
</html>
```